Holiday Sale 2026 Graphics for New Year

I want to create 10 social media graphics (new Instagram size 4:5 (1080 x 1350 pixels) focusing on our Holiday Sale Graphics, using any of the pics attached. Use the attached pics, NO RANDOM STOCK PHOTOGRAPHY. For the color scheme of the graphics, they should all be complementary to the product colors in the photos.
You can add any of the photos attached but none are required. You can do some of the graphics in all text. I mainly need BOLD text that says one of the headlines with the pics (10 total):
1. 25% OFF Holiday Sale: New You Starts Now!
2. 25% OFF Everything: New Year, New You
3. 25% OFF Christmas Sale 🎁 Feel Amazing Again!
4. Holiday Treat: 25% OFF Your Favorites
5. 25% OFF All Supplements ✨ New Year Reset!
6. Holiday Magic: 25% OFF Every Supplement
7. 25% OFF to Kickstart Your New Year Goals
8. New Year, New Waistline! 25% OFF Sale
9. Holiday Sale: 25% OFF Everything
10. A Better You Begins With 25% OFF

```html
<!DOCTYPE html>
<html lang="en">
<head>
<meta charset="utf-8">
<title>Holiday Sale Social Graphics</title>
<link rel="stylesheet" href="https://fonts.googleapis.com/css2?family=Oswald:wght@500;600;700&display=swap">
<style>
  :root{
    --page:#0f0f0f;
    --purple:#7c4a82;
    --purple-dark:#5e3563;
    --purple-soft:#9a6aa0;
    --red:#ee2a2c;
    --green:#2f5848;
    --blue:#3ea2ee;
    --white:#ffffff;
    --paper:#f1f1f1;
    --photo-warm:#8a5a4a;
    --photo-dark:#3b2a2a;
  }
  *{margin:0;padding:0;box-sizing:border-box}
  html,body{width:1200px;height:2775px;overflow:hidden;background:var(--page)}
  body{font-family:"Oswald",sans-serif;position:relative}
  .tile{position:absolute;width:385px;height:482px;overflow:hidden}
  .col-a{left:205px}.col-b{left:610px}
  .row-1{top:147px}.row-2{top:647px}.row-3{top:1143px}.row-4{top:1644px}.row-5{top:2143px}
  .bg-paper{background:linear-gradient(180deg,var(--white),var(--paper) 70%,#dcdcdc)}
  .bg-purple{background:linear-gradient(135deg,var(--purple),var(--purple-dark))}
  .abs{position:absolute}
  .txt{position:absolute;line-height:1;text-transform:uppercase;white-space:nowrap;font-weight:600}
  .white{color:var(--white)}.green{color:var(--green)}.purple{color:var(--purple)}.red{color:var(--red)}.blue{color:var(--blue)}
  .box{position:absolute;display:flex;align-items:center;justify-content:center;text-transform:uppercase;white-space:nowrap;font-weight:600;line-height:1}
  .box-red{background:var(--red);color:var(--white)}
  .box-green{background:var(--green);color:var(--white)}
  .box-blue{background:var(--blue);color:var(--white)}
  .shadow{box-shadow:0 10px 14px -8px rgba(0,0,0,.5)}
  .photo-person{position:absolute;background:linear-gradient(180deg,var(--photo-warm),var(--photo-dark) 60%,#e7e3e3)}
  .photo-bottles{position:absolute;border-radius:10px;background:linear-gradient(180deg,#fafafa,#d9d9de 80%,#b9b9c2)}
  .vertical{writing-mode:vertical-rl;transform:rotate(180deg)}
  .pct{display:flex;align-items:flex-start}
  .pct .num{font-weight:700;line-height:.82}
  .pct .side{display:flex;flex-direction:column;line-height:.85;font-weight:700}
</style>
</head>
<body>

<!-- 1 -->
<section class="tile col-a row-1 bg-paper">
  <div class="txt green" style="left:0;width:385px;text-align:center;top:24px;font-size:60px">25% OFF</div>
  <div class="box box-red shadow" style="left:33px;top:100px;width:318px;height:78px;font-size:50px">Holiday Sale</div>
  <div class="photo-bottles" role="img" aria-label="Row of four supplement bottles" style="left:30px;top:205px;width:325px;height:175px"></div>
  <div class="box box-green" style="left:68px;top:413px;width:248px;height:34px;font-size:20px;font-weight:500">New You Starts Now!</div>
</section>

<!-- 2 -->
<section class="tile col-b row-1 bg-purple">
  <div class="photo-person" role="img" aria-label="Smiling woman in a sheer black top holding supplement bottles" style="left:150px;top:0;width:235px;height:482px"></div>
  <div class="txt white" style="left:28px;top:24px;font-size:58px">25% OFF</div>
  <div class="txt blue vertical" style="left:20px;top:104px;height:356px;font-size:68px;text-align:left">Everything</div>
  <div class="box box-red" style="left:121px;top:430px;width:264px;height:52px;font-size:28px;font-weight:500">New Year, New You</div>
</section>

<!-- 3 -->
<section class="tile col-a row-2 bg-purple">
  <div class="photo-person" role="img" aria-label="Smiling woman in a white crop sweater behind a row of supplement bottles" style="left:190px;top:0;width:195px;height:482px"></div>
  <div class="pct white abs" style="left:26px;top:28px">
    <span class="num" style="font-size:142px">25</span>
    <span class="side"><span style="font-size:74px">%</span><span style="font-size:38px">OFF</span></span>
  </div>
  <div class="txt red" style="left:26px;top:162px;font-size:40px">Christmas</div>
  <div class="txt white" style="left:26px;top:205px;font-size:92px;font-weight:700">Sale</div>
  <div class="box box-blue shadow" style="left:30px;top:312px;width:126px;height:135px;font-size:30px;white-space:normal;text-align:center;flex-direction:column;line-height:1.15">Feel<br>Amazing<br>Again!</div>
</section>

<!-- 4 -->
<section class="tile col-b row-2 bg-paper">
  <div class="txt purple" style="left:0;width:385px;text-align:center;top:32px;font-size:56px">Holiday Treat</div>
  <div class="box box-red shadow" style="left:33px;top:95px;width:318px;height:92px;font-size:74px">25% OFF</div>
  <div class="photo-bottles" role="img" aria-label="Row of four supplement bottles" style="left:25px;top:220px;width:335px;height:165px"></div>
  <div class="box box-green" style="left:70px;top:408px;width:250px;height:35px;font-size:21px;font-weight:500">Your Favorites</div>
</section>

<!-- 5 -->
<section class="tile col-a row-3 bg-purple">
  <div class="abs" role="img" aria-label="Faint background photo of woman with supplement bottles" style="left:0;top:0;width:385px;height:482px;background:radial-gradient(circle at 60% 40%,var(--purple-soft),transparent 70%);opacity:.5"></div>
  <div class="pct white abs" style="left:50px;top:100px">
    <span class="num" style="font-size:168px">25</span>
    <span class="side"><span style="font-size:96px">%</span><span class="blue" style="font-size:60px">OFF</span></span>
  </div>
  <div class="txt white" style="left:0;width:385px;text-align:center;top:272px;font-size:42px;font-weight:500">All Supplements</div>
  <div class="box box-blue shadow" style="left:52px;top:395px;width:278px;height:45px;font-size:32px;font-weight:500">New Year Reset!</div>
</section>

<!-- 6 -->
<section class="tile col-b row-3 bg-purple">
  <div class="abs" role="img" aria-label="Faint supplement bottle in background" style="left:290px;top:130px;width:120px;height:190px;border-radius:14px;background:var(--purple-soft);opacity:.35"></div>
  <div class="txt white" style="left:0;width:385px;text-align:center;top:65px;font-size:54px;font-weight:500">Holiday Magic</div>
  <div class="abs" style="left:28px;top:137px;width:330px;height:2px;background:var(--blue)"></div>
  <div class="pct white abs" style="left:52px;top:155px">
    <span class="num" style="font-size:170px">25</span>
    <span class="side"><span style="font-size:98px">%</span><span class="blue" style="font-size:60px">OFF</span></span>
  </div>
  <div class="box box-blue shadow" style="left:0;top:368px;width:263px;height:58px;font-size:30px;font-weight:500">Every Supplement</div>
</section>

<!-- 7 -->
<section class="tile col-a row-4" style="background:var(--white)">
  <div class="abs" style="left:0;top:372px;width:385px;height:110px;background:var(--purple)"></div>
  <div class="pct purple abs" style="left:24px;top:20px">
    <span class="num" style="font-size:160px">25</span>
    <span class="side"><span style="font-size:96px">%</span><span style="font-size:52px">OFF TO</span></span>
  </div>
  <div class="box box-red shadow" style="left:26px;top:180px;width:331px;height:76px;font-size:64px;font-weight:700">Kickstart</div>
  <div class="txt green" style="left:0;width:385px;text-align:center;top:265px;font-size:34px;text-transform:none">Your New Year Goals</div>
  <div class="photo-bottles" role="img" aria-label="Supplement bottles arranged on a white cloth" style="left:45px;top:312px;width:315px;height:165px"></div>
</section>

<!-- 8 -->
<section class="tile col-b row-4 bg-purple">
  <div class="photo-person" role="img" aria-label="Smiling woman in a white crop sweater behind supplement bottles" style="left:200px;top:0;width:185px;height:482px"></div>
  <div class="txt white" style="left:26px;top:32px;font-size:62px">New Year,</div>
  <div class="txt white" style="left:26px;top:95px;font-size:38px">New Waistline!</div>
  <div class="pct white abs" style="left:26px;top:150px">
    <span class="num" style="font-size:124px">25</span>
    <span class="side"><span style="font-size:72px">%</span><span style="font-size:40px">OFF</span></span>
  </div>
  <div class="box box-blue shadow" style="left:0;top:292px;width:165px;height:55px;font-size:40px;font-weight:500;justify-content:flex-start;padding-left:28px">Sale</div>
</section>

<!-- 9 -->
<section class="tile col-a row-5 bg-purple">
  <div class="photo-person" role="img" aria-label="Smiling woman in a sheer black top holding supplement bottles" style="left:115px;top:0;width:270px;height:482px"></div>
  <div class="txt white vertical" style="left:22px;top:18px;height:450px;font-size:74px;text-align:left">Holiday Sale</div>
  <div class="box box-red" style="left:146px;top:430px;width:239px;height:50px;font-size:24px;font-weight:500">25% OFF Everything</div>
</section>

<!-- 10 -->
<section class="tile col-b row-5 bg-paper">
  <div class="abs" style="left:0;top:408px;width:385px;height:74px;background:var(--purple)"></div>
  <div class="txt green" style="left:26px;top:40px;font-size:58px">A Better You</div>
  <div class="txt green" style="left:26px;top:106px;font-size:58px">Begins With</div>
  <div class="box box-red shadow" style="left:26px;top:184px;width:330px;height:85px;font-size:72px">25% OFF</div>
  <div class="photo-bottles" role="img" aria-label="Row of four supplement bottles" style="left:30px;top:290px;width:330px;height:175px"></div>
</section>

</body>
</html>
```